Home Services Website Design and Revisions

We have started to create a website but I would like to get some ideas and a quote on how to create a more professional website then what we have created thus far.

http://brinkhavenhomecare.example/

Pages I would need on the site

Home page - company summary and brand promise
who we are
what we do - services offered
our promise to quality and client experience
client experiences - testimonials and pictures
Promotions
Career opportunities - Join The team
Updates

Target Market(s)

Homeowners in the DFW region

Industry/Entity Type

Home Improvement

Number of Pages Required

5+ page

Font styles to use
Sans Serif

Requirements
Must have
• Home page - company summary and brand promise
• who we are
• what we do - services offered
• our promise to quality and client experience
• client experiences - testimonials and pictures
• Promotions
• Career opportunities - Join The team
• logo
• pictures
• links to social media sites
• A very impactful home page
• With a image of home and family.
• a beautiful home, yard and pictures of a loving family smiling and enjoying their home.
Nice to have
• Pictures with people to create emotion
• we don't work on houses
• we work on homes with families that trust us to provide quality services in a timely manner
• Families that trust us as their partner when they need work at their home with their family
Should not have
• low quality images or images just of homes

```html
<!DOCTYPE html>
<html lang="en">
<head>
<meta charset="utf-8">
<title>Brinkhaven – Painting and Home Services Experts</title>
<link rel="stylesheet" href="https://fonts.googleapis.com/css2?family=Open+Sans:ital,wght@0,400;0,600;0,700;1,400&family=Raleway:wght@500;600;700&display=swap">
<style>
:root{
  --gold:#f2bb1d;
  --gold-deep:#e9ad0c;
  --ink:#222222;
  --text:#3a3a3a;
  --muted:#8f8f8f;
  --line:#dcdcdc;
  --band:#f1f1f1;
  --topbar:#232323;
  --footer:#333333;
  --footer-base:#2a2a2a;
  --white:#ffffff;
}
*{box-sizing:border-box;margin:0;padding:0}
html,body{width:1200px;height:2338px;overflow:hidden}
body{position:relative;background:var(--white);font-family:"Open Sans",Arial,sans-serif;color:var(--text)}
.abs{position:absolute}

/* top bar */
.topbar{left:0;top:0;width:1200px;height:117px;background:var(--topbar)}
.toplinks{right:100px;top:22px;display:flex;gap:16px;font-size:10px;color:var(--white);text-transform:uppercase}
.toplinks span.sep{color:#aaa}

/* header card */
.brandbar{left:100px;top:56px;width:1000px;height:128px;background:linear-gradient(115deg,var(--gold-deep) 0 47%,var(--gold) 47% 100%)}
.brand{left:36px;top:40px;display:flex;align-items:center;gap:10px}
.brand-mark{width:22px;height:22px;background:var(--ink)}
.brand-name{font-weight:700;font-size:30px;color:var(--ink);letter-spacing:.5px}
.brand-line{left:36px;top:84px;font-size:7px;font-weight:700;color:var(--ink);letter-spacing:.3px}
.reach{top:44px;display:flex;align-items:center;gap:14px;color:var(--white)}
.reach .ring{width:40px;height:40px;border:1.5px solid rgba(255,255,255,.85);border-radius:50%;display:flex;align-items:center;justify-content:center}
.reach .lbl{font-size:11px;font-weight:600;text-transform:uppercase}
.reach .val{font-size:12px;margin-top:3px}
.reach.call{left:510px}
.reach.mail{left:710px}

.nav{left:100px;top:184px;width:1000px;height:61px;background:var(--white);box-shadow:0 4px 10px rgba(0,0,0,.12);display:flex;align-items:center;padding-left:36px;gap:40px;font-size:11.5px;font-weight:600;color:var(--ink);text-transform:uppercase;z-index:3}
.nav .active{color:var(--gold-deep)}

/* hero */
.hero{left:0;top:218px;width:1200px;height:514px;background:linear-gradient(180deg,#cfc7bc 0%,#a89a89 45%,#7a6350 80%,#5c4332 100%)}
.hero-copy{left:0;top:378px;width:1200px;text-align:center;color:var(--white)}
.hero-name{font-size:54px;font-weight:700;letter-spacing:1px;line-height:1}
.hero-tag{margin-top:18px;font-size:17px;font-weight:700;text-transform:uppercase}
.hero-services{margin-top:8px;font-size:9px;text-transform:uppercase;letter-spacing:.4px}
.hero-actions{margin-top:16px;display:flex;justify-content:center;gap:14px}
.btn{display:inline-block;height:36px;line-height:36px;padding:0 27px;font-size:11px;font-weight:700;text-transform:uppercase;min-width:126px;text-align:center}
.btn-gold{background:var(--gold);color:var(--white);box-shadow:0 2px 0 #c99606}
.btn-light{background:var(--white);color:var(--gold-deep);border:1px solid var(--gold)}

/* section headings */
.sec-title{left:0;width:1200px;text-align:center;font-size:23px;font-weight:700;color:var(--gold-deep);text-transform:uppercase}
.sec-sub{left:0;width:1200px;text-align:center;font-size:9.5px;color:#555;text-transform:uppercase}

/* services */
.service{top:865px;width:300px;text-align:center}
.service .icon{width:88px;height:88px;margin:0 auto;border:3px solid var(--gold);border-radius:50%;display:flex;align-items:center;justify-content:center}
.service h3{margin-top:20px;font-family:"Raleway",Arial,sans-serif;font-weight:500;font-size:19px;color:#444}
.service p{margin:14px auto 0;width:290px;font-size:12px;line-height:22px;color:var(--muted)}
.service a{display:inline-block;margin-top:10px;font-size:13px;color:#666;text-decoration:underline}
.arrow{font-size:40px;color:#d8d8d8;font-weight:400}

/* projects */
.projects{left:0;top:1184px;width:1200px;height:605px;background:var(--band)}
.filters{left:100px;top:1308px;display:flex;gap:4px}
.filters span{height:28px;line-height:26px;padding:0 12px;font-size:10px;text-transform:uppercase;color:#aaa;border:1px solid var(--line);background:var(--white)}
.filters span.on{background:var(--gold);color:var(--white);border-color:var(--gold);font-weight:700}
.tile{width:243px;height:165px}

/* testimonials */
.quote{top:1910px;width:520px}
.quote .photo{position:absolute;left:0;top:5px;width:88px;height:88px;border-radius:50%;border:3px solid #e6e6e6}
.quote .mark{position:absolute;font-size:36px;color:#cfcfcf;font-family:Georgia,serif;line-height:1}
.quote p{position:absolute;left:122px;top:8px;width:390px;font-style:italic;font-size:12px;line-height:24px;color:var(--muted)}
.quote .who{position:absolute;left:113px;top:85px;font-size:14px;color:#555}
.quote .who b{color:var(--gold-deep);font-weight:700;font-family:"Raleway",Arial,sans-serif}

/* footer */
.footer{left:0;top:2088px;width:1200px;height:187px;background:var(--footer)}
.footbase{left:0;top:2275px;width:1200px;height:63px;background:var(--footer-base);border-top:1px solid #444;text-align:center;color:#ddd;font-size:11.5px;line-height:63px}
.f-head{font-family:"Raleway",Arial,sans-serif;font-weight:600;font-size:15px;color:var(--white);text-transform:uppercase}
.f-row{display:flex;gap:20px;font-size:12px;color:#ddd;line-height:20px}
.f-row svg{flex:none;margin-top:3px}
.news{left:462px;top:2152px;display:flex;gap:8px}
.news .field{width:247px;height:40px;background:var(--white);font-size:11px;color:#777;padding-left:14px;line-height:40px}
.news .btn{height:40px;line-height:40px;min-width:90px;padding:0 10px;font-size:10.5px}
.social{left:950px;top:2153px;display:flex;gap:6px}
.social span{width:26px;height:26px;border:1.5px solid var(--white);border-radius:50%}
</style>
</head>
<body>

<div class="abs topbar"></div>
<div class="abs toplinks"><span>Site Map</span><span class="sep">|</span><span>Information</span><span class="sep">|</span><span>Extras</span></div>

<div class="abs hero" role="img" aria-label="Bright empty living room with tall white-framed windows, chandelier, fireplace and hardwood floor"></div>

<header class="abs brandbar">
  <div class="abs brand"><span class="brand-mark"></span><span class="brand-name">BRINKHAVEN</span></div>
  <div class="abs brand-line">PAINTING AND HOME SERVICES EXPERTS</div>
  <div class="abs reach call">
    <div class="ring"><svg width="16" height="16" viewBox="0 0 24 24"><path d="M6.6 10.8a15.1 15.1 0 0 0 6.6 6.6l2.2-2.2a1 1 0 0 1 1-.25 11.4 11.4 0 0 0 3.6.57 1 1 0 0 1 1 1V20a1 1 0 0 1-1 1A17 17 0 0 1 3 4a1 1 0 0 1 1-1h3.5a1 1 0 0 1 1 1c0 1.25.2 2.45.57 3.57a1 1 0 0 1-.25 1z" fill="#fff"/></svg></div>
    <div><div class="lbl">Call us :</div><div class="val">+ 555 0142 318</div></div>
  </div>
  <div class="abs reach mail">
    <div class="ring"><svg width="16" height="14" viewBox="0 0 24 20"><rect x="1" y="2" width="22" height="16" rx="2" fill="#fff"/><path d="M2 4l10 7 10-7" stroke="#e9ad0c" stroke-width="2" fill="none"/></svg></div>
    <div><div class="lbl">Email us :</div><div class="val">info@brinkhavenhomecare.example</div></div>
  </div>
</header>

<nav class="abs nav">
  <span class="active">Home</span><span>Who we are</span><span>What we do</span><span>Client experiences</span><span>Promotions</span><span>Career opportunities</span><span>Contact us</span>
  <svg width="12" height="12" viewBox="0 0 24 24"><circle cx="10" cy="10" r="7" stroke="#e9ad0c" stroke-width="3" fill="none"/><path d="M15 15l7 7" stroke="#e9ad0c" stroke-width="3"/></svg>
</nav>

<section class="abs hero-copy">
  <div class="hero-name">BRINKHAVEN</div>
  <div class="hero-tag">Painting and Home Services Experts</div>
  <div class="hero-services">• Painting &nbsp;• Landscaping/Mowing &nbsp;• Window Washing &nbsp;• Maid Services</div>
  <div class="hero-actions"><span class="btn btn-gold">Read more</span><span class="btn btn-light">Contact</span></div>
</section>

<!-- what we do -->
<h2 class="abs sec-title" style="top:776px">What we do</h2>
<div class="abs sec-sub" style="top:814px">We understand the importance of home and family</div>
<div class="abs arrow" style="left:44px;top:948px">‹</div>
<div class="abs arrow" style="left:1133px;top:948px">›</div>

<div class="abs service" style="left:110px">
  <div class="icon"><svg width="40" height="40" viewBox="0 0 40 40"><rect x="6" y="14" width="10" height="22" fill="none" stroke="#e9ad0c" stroke-width="2"/><rect x="16" y="4" width="12" height="32" fill="none" stroke="#e9ad0c" stroke-width="2"/><rect x="28" y="18" width="7" height="18" fill="none" stroke="#e9ad0c" stroke-width="2"/><path d="M19 9h6M19 14h6M19 19h6M19 24h6M9 19h4M9 24h4" stroke="#e9ad0c" stroke-width="2"/></svg></div>
  <h3>Exterior Painting</h3>
  <p>At BRINKHAVEN we understand the importance of home and family. We work to ensure your</p>
  <a>Read More</a>
</div>
<div class="abs service" style="left:450px">
  <div class="icon"><svg width="40" height="40" viewBox="0 0 40 40"><rect x="9" y="5" width="22" height="31" fill="none" stroke="#555" stroke-width="2"/><path d="M13 11h14M13 17h14M13 23h14" stroke="#e9ad0c" stroke-width="3"/><rect x="17" y="28" width="6" height="8" fill="#555"/></svg></div>
  <h3>Interior Painting</h3>
  <p>At BRINKHAVEN we understand the importance of home and family. We work to ensure your</p>
  <a>Read More</a>
</div>
<div class="abs service" style="left:790px">
  <div class="icon"><svg width="40" height="40" viewBox="0 0 40 40"><path d="M4 18L20 6l16 12" fill="none" stroke="#555" stroke-width="2"/><rect x="8" y="18" width="24" height="16" fill="none" stroke="#555" stroke-width="2"/><path d="M12 22h6v5h-6zM22 22h6v5h-6z" fill="#e9ad0c"/></svg></div>
  <h3>Commercial Painting</h3>
  <p>At BRINKHAVEN we understand the importance of home and family. We work to ensure your</p>
  <a>Read More</a>
</div>
<div class="abs" style="left:543px;top:1094px"><span class="btn btn-gold" style="width:120px;height:40px;line-height:40px">View more</span></div>

<!-- latest projects -->
<section class="abs projects"></section>
<h2 class="abs" style="left:98px;top:1228px;font-size:23px;font-weight:700;color:var(--gold-deep)">LATEST PROJECTS</h2>
<div class="abs" style="left:100px;top:1265px;font-size:9.5px;color:#555">WE UNDERSTAND THE IMPORTANCE OF HOME AND FAMILY</div>
<div class="abs filters"><span class="on">All works</span><span>Landscaping</span><span>Fence</span><span>Window</span><span>Commercial</span></div>

<div class="abs tile" style="left:100px;top:1371px;background:linear-gradient(160deg,#6e8db3,#8a5a3a 60%,#c9a77a)" role="img" aria-label="Victorian house painted in brick red and cream with colour swatches"></div>
<div class="abs tile" style="left:352px;top:1371px;background:linear-gradient(180deg,#8fb3d4,#b8a585 55%,#7a7a6a)" role="img" aria-label="Large stone two-storey home with turret"></div>
<div class="abs tile" style="left:604px;top:1371px;background:linear-gradient(180deg,#d8d0c4,#a99682 60%,#7a5a3e)" role="img" aria-label="Freshly painted living room with fireplace"></div>
<div class="abs tile" style="left:857px;top:1371px;background:linear-gradient(180deg,#9bc0e0,#7d9a5a 45%,#8a4a35)" role="img" aria-label="Landscaped flower bed beside a brick house"></div>
<div class="abs tile" style="left:100px;top:1546px;background:linear-gradient(180deg,#6ea24a,#3f7a2a)" role="img" aria-label="Red lawn mower on freshly cut grass"></div>
<div class="abs tile" style="left:352px;top:1546px;background:linear-gradient(180deg,#a8b39a,#5d7d3a 50%,#4a3a2a)" role="img" aria-label="Garden steps with shrubs and mulch beds"></div>
<div class="abs tile" style="left:604px;top:1546px;background:linear-gradient(180deg,#a4b5c6,#7a7268 50%,#5a5048)" role="img" aria-label="Worker on a ladder washing second-storey windows"></div>
<div class="abs tile" style="left:857px;top:1546px;background:linear-gradient(180deg,#c8d0d8,#9a8064 55%,#6a5a48)" role="img" aria-label="Window washers working on a brick family home"></div>

<!-- client experiences -->
<h2 class="abs sec-title" style="top:1824px">Client experiences</h2>
<div class="abs sec-sub" style="top:1862px">We understand the importance of home and family</div>
<div class="abs arrow" style="left:44px;top:1925px;font-size:30px">‹</div>
<div class="abs arrow" style="left:1138px;top:1925px;font-size:30px">›</div>

<div class="abs quote" style="left:98px">
  <div class="photo" style="background:linear-gradient(180deg,#d9b48a,#b98a60)" role="img" aria-label="Portrait of a smiling client"></div>
  <span class="mark" style="left:112px;top:0">“</span>
  <p>Esearching contractors in the area, scheduling estimates, meeting contractors, dealing with no shows, and then hoping for top quality services</p>
  <span class="mark" style="left:330px;top:62px">”</span>
  <div class="who"><b>Marcus Hale,</b> CEO</div>
</div>
<div class="abs quote" style="left:622px">
  <div class="photo" style="background:linear-gradient(180deg,#5a4a40,#a57a5a)" role="img" aria-label="Portrait of a smiling client"></div>
  <span class="mark" style="left:112px;top:0">“</span>
  <p>Esearching contractors in the area, scheduling estimates, meeting contractors, dealing with no shows, and then hoping for top quality services</p>
  <span class="mark" style="left:330px;top:62px">”</span>
  <div class="who"><b>Marcus Hale,</b> CEO</div>
</div>

<!-- footer -->
<footer class="abs footer"></footer>
<div class="abs f-head" style="left:99px;top:2118px">Contact us</div>
<div class="abs" style="left:98px;top:2153px;display:flex;flex-direction:column;gap:12px">
  <div class="f-row"><svg width="12" height="14" viewBox="0 0 24 28"><path d="M12 0a9 9 0 0 0-9 9c0 7 9 17 9 17s9-10 9-17a9 9 0 0 0-9-9zm0 12a3 3 0 1 1 0-6 3 3 0 0 1 0 6z" fill="#fff"/></svg><span>Street Name.City Name ,Country Name<br>Zip Code 4579815.</span></div>
  <div class="f-row"><svg width="12" height="12" viewBox="0 0 24 24"><path d="M6.6 10.8a15.1 15.1 0 0 0 6.6 6.6l2.2-2.2a1 1 0 0 1 1-.25 11.4 11.4 0 0 0 3.6.57 1 1 0 0 1 1 1V20a1 1 0 0 1-1 1A17 17 0 0 1 3 4a1 1 0 0 1 1-1h3.5a1 1 0 0 1 1 1c0 1.25.2 2.45.57 3.57a1 1 0 0 1-.25 1z" fill="#fff"/></svg><span>+ 555 0186 240</span></div>
  <div class="f-row"><svg width="14" height="11" viewBox="0 0 24 20"><rect x="1" y="2" width="22" height="16" rx="2" fill="#fff"/><path d="M2 4l10 7 10-7" stroke="#333" stroke-width="2" fill="none"/></svg><span>brinkhavenhomecare.example</span></div>
</div>

<div class="abs f-head" style="left:462px;top:2118px">News letter</div>
<div class="abs news"><div class="field">Email:</div><span class="btn btn-gold">Subscribe</span></div>
<div class="abs" style="left:462px;top:2204px;font-size:10px;font-style:italic;color:#ccc">* best time to contact you back!</div>

<div class="abs f-head" style="left:950px;top:2118px">Follow us</div>
<div class="abs social"><span></span><span></span><span></span><span></span><span></span></div>

<div class="abs footbase">Copyright © 2016 brinkhavenhomecare.example. All Rights are Reserved</div>

</body>
</html>
```